Qel Programming Video Tutorial Blog

Please be aware I am flexible with budget, I will increase it for great design thanks

A blog (wordpress) design required for video blogging teaching Qel Programming (creating ravlet apps). There are 4 pages required to be designed, the landing page where user submit their name and email (also shows an intro video), the main video blogging page (with beautiful video placeholder), a normal text blog page with big image at the top of each post and finally the portfolio page. The portfolio is where the tutor showcase all his previous developed apps and other projects to show his expertise.

The colour combination preferred are a mixture of blue and orange but we are open to other beautiful color combinations. Minimalistic design with lots of white and clare objectives for each page. The design should reflect the purpose of the website, someone who cannot read english landing on the page should immediately realise the page is made for learning to design ravlet apps.

I like curves and round corners, especially comment and portfolio pages with curves etc thanks

The blog domain will be quibnest.com

Target Market(s)

new programmer on the ravlet platform

Industry/Entity Type

Learning

Requirements
Must have
• ravlet image in the design
landing page has a video intro and Ravlet/mork image
Nice to have
• curves. round corners and circular shapes

```html
<!DOCTYPE html>
<html lang="en">
<head>
<meta charset="utf-8">
<title>Quibnest – Video Blogging Teaching Qel Programming</title>
<link href="https://fonts.googleapis.com/css2?family=Fredoka:wght@500;600&family=Kaushan+Script&family=Arimo:wght@400;700&display=swap" rel="stylesheet">
<style>
:root{
  --blue:#00aeef;
  --blue-dark:#0a7fb3;
  --orange:#f7a600;
  --orange-dark:#d38a00;
  --ink:#111;
  --heading:#444;
  --hint:#777;
  --panel:#fff;
  --section:#e9e9e9;
  --footer:#000;
  --footer-icon:#333;
}
*{box-sizing:border-box;margin:0;padding:0}
html,body{width:1200px;height:1001px;overflow:hidden}
body{position:relative;font-family:Arimo,Arial,sans-serif;background:var(--section);color:var(--ink)}
.abs{position:absolute}

.site-header{left:0;top:0;width:1200px;height:75px;background:var(--blue)}
.brand{left:174px;top:18px;font-family:Fredoka,sans-serif;font-weight:600;font-size:31px;color:#fff;display:flex;align-items:center;gap:9px}
.brand-dot{width:22px;height:22px;border-radius:50%;background:#fff}
.social-top{top:14px;left:839px;display:flex;gap:5px}
.social-top span{width:20px;height:20px;border-radius:50%;background:#4dc6f3}
.auth{left:914px;top:14px;height:20px;display:flex;font-size:11px;border-radius:3px;overflow:hidden}
.auth span{display:flex;align-items:center;padding:0 8px;color:#fff}
.auth .signin{background:var(--orange);width:55px;justify-content:center}
.auth .signup{background:var(--blue-dark);width:58px;justify-content:center}
.main-nav{top:46px;left:676px;display:flex;gap:0;font-family:Fredoka,sans-serif;font-weight:500;font-size:14.5px;color:#fff;letter-spacing:.2px}
.main-nav a{color:#fff;text-decoration:none}
.main-nav .n1{margin-right:31px}.main-nav .n2{margin-right:23px}.main-nav .n3{margin-right:24px}

.hero{left:0;top:75px;width:1200px;height:432px;background:linear-gradient(180deg,#fafafa 0%,#e4e4e4 45%,#f2f2f2 100%)}
.hero-title{left:0;top:106px;width:1200px;text-align:center;font-family:Fredoka,sans-serif;font-weight:600;font-size:40px;color:var(--blue);letter-spacing:-.3px}
.hero-text{left:250px;top:163px;width:700px;text-align:center;font-size:13.5px;line-height:17px;color:var(--ink)}
.hero-text .more{display:inline-block;width:13px;height:13px;border-radius:50%;background:var(--orange);vertical-align:-2px;margin-left:5px;position:relative}
.hero-text .more:after{content:"";position:absolute;left:3px;top:3.5px;border-left:6px solid #fff;border-top:3px solid transparent;border-bottom:3px solid transparent}

.tablet{left:233px;top:220px;width:738px;height:287px;border-radius:34px 34px 0 0;background:#cfcfcf;padding:5px 5px 0}
.tablet-body{width:100%;height:100%;border-radius:30px 30px 0 0;background:#1c1c1c}
.video{left:301px;top:279px;width:604px;height:228px;background:linear-gradient(160deg,#6b6e72 0%,#3f4448 45%,#5a3a35 80%,#2c2f33 100%)}
.status{left:301px;top:279px;width:604px;height:12px;background:#000;color:#ddd;font-size:7px;display:flex;justify-content:center;align-items:center}
.play{left:575px;top:355px;width:50px;height:50px}
.video-caption{left:500px;top:414px;width:200px;text-align:center;font-family:"Kaushan Script",cursive;font-size:14px;color:#fff}
.dots{left:587px;top:478px;display:flex;gap:3px}
.dots span{width:7px;height:7px;border-radius:50%;background:#fff}
.dots span:first-child{background:var(--blue)}

.signup-section{left:0;top:507px;width:1200px;height:414px;background:var(--section);border-top:1px solid #d6d6d6}
.down-arrow{left:594px;top:524px}
.section-title{left:0;top:553px;width:1200px;text-align:center;font-family:Fredoka,sans-serif;font-weight:600;font-size:29px;color:var(--heading)}
.all-fields{left:876px;top:597px;font-size:8.5px;color:var(--hint)}
.all-fields b{color:#f05a00;font-weight:400}
.form-card{left:248px;top:613px;width:720px;height:253px;background:var(--panel);border-radius:4px;box-shadow:0 0 3px rgba(0,0,0,.2)}
.field{height:34px;border:1px solid #c8c8c8;border-radius:4px;background:#fff;font-size:14.5px;color:#777;display:flex;align-items:center;padding-left:15px}
.field.is-focus{background:#eef8fd;border-color:#aac9d8;color:#9ab}
.field.is-error{background:#fff5e1;border-color:#f0c77a;color:#a89a80}
.hint{font-size:8.5px;color:var(--hint)}
.go-next{left:536px;top:850px;width:134px;height:31px;border-radius:16px;background:var(--orange);border-bottom:3px solid var(--orange-dark);color:#fff;font-family:Fredoka,sans-serif;font-weight:600;font-size:18px;display:flex;align-items:center;justify-content:center;gap:6px}

.site-footer{left:0;top:921px;width:1200px;height:80px;background:var(--footer);color:#fff;font-size:12px}
.foot-links{left:173px;top:29px;line-height:17px}
.foot-links a{color:#fff;text-decoration:none}
.foot-links .mail{color:var(--blue)}
.social-foot{left:896px;top:21px;display:flex;gap:8px}
.social-foot span{width:38px;height:38px;border-radius:50%;background:var(--footer-icon)}
</style>
</head>
<body>
<header class="abs site-header">
  <div class="abs brand"><span class="brand-dot"></span>Quibnest</div>
  <div class="abs social-top"><span></span><span></span><span></span></div>
  <div class="abs auth"><span class="signin">SIGNIN</span><span class="signup">SIGNUP</span></div>
  <nav class="abs main-nav"><a class="n1">HOME</a><a class="n2">ABOUT DEVELOPER</a><a class="n3">BLOG</a><a>CONTACT</a></nav>
</header>

<section class="abs hero">
</section>
<h1 class="abs hero-title">Video Blogging Teaching Qel Programming</h1>
<p class="abs hero-text">Lorem ipsum dolor sit amet, consectetur adipisicing elit, sed do eiusmod tempor incididunt ut labore et dolore magna aliqua. Ut enim ad minim veniam, quis nostrud Lorem ipsum dolor sit ame<span class="more"></span></p>

<div class="abs tablet" role="img" aria-label="Mork tablet showing the intro video"><div class="tablet-body"></div></div>
<div class="abs video" role="img" aria-label="Intro video still: developers working at desks in an office"></div>
<div class="abs status">4:15 PM</div>
<svg class="abs play" viewBox="0 0 50 50"><circle cx="25" cy="25" r="22.5" fill="none" stroke="#fff" stroke-width="3"/><path d="M19 14 L36 25 L19 36 Z" fill="#fff"/></svg>
<div class="abs video-caption">This is our intro video</div>
<div class="abs dots"><span></span><span></span><span></span></div>

<section class="abs signup-section"></section>
<svg class="abs down-arrow" width="14" height="34" viewBox="0 0 14 34"><line x1="7" y1="0" x2="7" y2="30" stroke="var(--blue)" stroke-width="1.5"/><path d="M2 25 L7 32 L12 25" fill="none" stroke="var(--blue)" stroke-width="1.5"/></svg>
<h2 class="abs section-title">Get your own website in seconds</h2>
<div class="abs all-fields">All fields <b>*</b></div>

<form class="abs form-card"></form>
<div class="abs field is-focus" style="left:310px;top:652px;width:269px">Username</div>
<div class="abs hint" style="left:315px;top:690px">(Must be at least 4 characters, letters and numbers only.)</div>
<div class="abs field is-error" style="left:600px;top:652px;width:267px">Invalid Email</div>
<div class="abs hint" style="left:601px;top:690px">(Must be at least 4 characters, letters and numbers only.)</div>
<div class="abs field" style="left:310px;top:717px;width:561px">Password</div>
<div class="abs hint" style="left:310px;top:756px">We send your registration email to this address. (Double-check your email address before continuing.)</div>
<div class="abs field" style="left:310px;top:778px;width:561px">Confirm</div>
<div class="abs hint" style="left:310px;top:822px">(Type your new password again.)</div>
<div class="abs go-next">Go Next <svg width="16" height="10" viewBox="0 0 16 10"><line x1="0" y1="5" x2="14" y2="5" stroke="#fff" stroke-width="1.6"/><path d="M10 1 L15 5 L10 9" fill="none" stroke="#fff" stroke-width="1.6"/></svg></div>

<footer class="abs site-footer">
  <div class="abs foot-links">
    <div><a>Home</a> &nbsp;-&nbsp; <a>About</a> &nbsp;-&nbsp; <a>Blog</a> &nbsp;-&nbsp; <a>Contact</a></div>
    <div>© 2013 &nbsp;-&nbsp; <a>Terms and Conditions</a> &nbsp; - &nbsp; Email : <a class="mail">info@quibnest.com</a></div>
  </div>
  <div class="abs social-foot"><span></span><span></span><span></span></div>
</footer>
</body>
</html>
```